Construction Company

I'm a new construction company called Tembrik Construction. I want my card to look simple and clean. I have provided a sample of what I want the front to look like (Tembrik_Card.jpeg) and a back ground for the back of the (Tembrik_Card_Background.jpeg) - the background can be faded so my name and other information is more prominent.
Construction

```html
<!DOCTYPE html>
<html lang="en">
<head>
<meta charset="utf-8">
<title>Tembrik Construction – Business Card</title>
<link rel="stylesheet" href="https://fonts.googleapis.com/css2?family=Arimo:wght@400;700&display=swap">
<style>
  :root {
    --page: #ffffff;
    --ink: #000000;
    --text: #231f20;
    --accent: #f7941d;
    --paper: #ffffff;
    --plan: #e9e9e9;
    --rule: #333333;
  }
  * { box-sizing: border-box; margin: 0; padding: 0; }
  html, body {
    width: 1200px;
    height: 1000px;
    overflow: hidden;
    background: var(--page);
    font-family: "Arimo", Arial, sans-serif;
  }
  .canvas {
    position: relative;
    width: 1200px;
    height: 1000px;
  }

  /* Front of card */
  .card-front {
    position: absolute;
    left: 214px;
    top: 20px;
    width: 806px;
    height: 460px;
    background: var(--ink);
  }
  .front-brand {
    position: absolute;
    left: 0;
    width: 100%;
    text-align: center;
    color: var(--accent);
    font-weight: 400;
  }
  .front-brand__name {
    top: 92px;
    font-size: 168px;
    line-height: 1;
    letter-spacing: -4px;
  }
  .front-brand__trade {
    top: 336px;
    font-size: 26px;
    line-height: 1;
    letter-spacing: 33px;
    padding-left: 33px;
  }

  /* Back of card */
  .card-back {
    position: absolute;
    left: 214px;
    top: 527px;
    width: 806px;
    height: 461px;
    background: var(--paper);
    border: 1px solid var(--rule);
    overflow: hidden;
  }
  .card-back__art {
    position: absolute;
    inset: 0;
    width: 100%;
    height: 100%;
  }
  .back-brand {
    position: absolute;
    left: 25px;
    color: var(--accent);
    font-weight: 400;
    line-height: 1;
  }
  .back-brand__name {
    top: 22px;
    font-size: 58px;
    letter-spacing: -1px;
  }
  .back-brand__trade {
    top: 85px;
    font-size: 9px;
    letter-spacing: 10.6px;
  }
  .holder-name {
    position: absolute;
    left: 346px;
    top: 84px;
    font-size: 46px;
    font-weight: 700;
    color: var(--text);
    line-height: 1;
  }
  .holder-rule {
    position: absolute;
    left: 250px;
    top: 145px;
    width: 556px;
    height: 5px;
    background: var(--accent);
  }
  .holder-position {
    position: absolute;
    left: 340px;
    top: 165px;
    font-size: 30px;
    font-weight: 400;
    color: var(--text);
    line-height: 1;
  }
  .contact-list {
    position: absolute;
    left: 340px;
    top: 290px;
    list-style: none;
    font-size: 20px;
    line-height: 30px;
    color: var(--text);
  }
  .contact-list__label { font-weight: 700; }
</style>
</head>
<body>
<main class="canvas">

  <section class="card-front" aria-label="Card front">
    <div class="front-brand front-brand__name">tembrik</div>
    <div class="front-brand front-brand__trade">CONSTRUCTION</div>
  </section>

  <section class="card-back" aria-label="Card back">
    <svg class="card-back__art" viewBox="0 0 806 461" preserveAspectRatio="none" aria-hidden="false">
      <defs>
        <linearGradient id="plan-fade" x1="0" y1="0" x2="1" y2="1">
          <stop offset="0" stop-color="#f1f1f1"/>
          <stop offset="1" stop-color="#f7f7f7"/>
        </linearGradient>
        <linearGradient id="edge-shadow" x1="0" y1="0" x2="1" y2="0">
          <stop offset="0" stop-color="#000" stop-opacity="0.35"/>
          <stop offset="1" stop-color="#000" stop-opacity="0"/>
        </linearGradient>
      </defs>
      <rect x="226" y="0" width="560" height="448" fill="url(#plan-fade)" opacity="0.8"
            role="img" aria-label="Faded architectural floor plan background"/>
      <polygon points="304,0 358,0 190,461 136,461" fill="url(#edge-shadow)" opacity="0.6"/>
      <polygon points="0,0 304,0 136,461 0,461" fill="#000000"/>
    </svg>

    <div class="back-brand back-brand__name">tembrik</div>
    <div class="back-brand back-brand__trade">CONSTRUCTION</div>

    <h1 class="holder-name">Your Name</h1>
    <div class="holder-rule"></div>
    <p class="holder-position">your position</p>

    <ul class="contact-list">
      <li><span class="contact-list__label">phone:</span> 123 456 789</li>
      <li><span class="contact-list__label">email:</span> yourname@domain.com</li>
      <li><span class="contact-list__label">address:</span> somewhere</li>
      <li><span class="contact-list__label">URL:</span> www.yoursite.com</li>
    </ul>
  </section>

</main>
</body>
</html>
```